Service Plan Sales Flyer

The Watchpost Depot (www.kelvamart.com) is a commercial security integrator that installs security cameras, access control, intrusion, two-way radios and perimeter security. We require a one page flyer for our service plan for new and existing customers. The price of the service plan is $299/yr and includes the following;
1. Discounted service rate of $118/hr
2. Free remote support ($85/hr without a plan)
3. Free remote training
4. Priority support

Please review our brochure attached and create a one page sales flyer with the end goal of having the client sign up for our annual service plan . The plan will automatically renew every year. Email sales@kelvamart.com.

Target Market(s)

commercial industrial clients - no residential

Industry/Entity Type

review our website at www.kelvamart.com

Colors
0054AA
0677BA
7BADD7
CADEEF
E8F1F8
EE7325
F08F49
F5BC92
FAE3D3
FDF4ED

Requirements
Must have
• call to action
Should not have
• too many colors

```html
<!DOCTYPE html>
<html lang="en">
<head>
<meta charset="utf-8">
<title>The Watchpost Depot – Annual Service Plan</title>
<link href="https://fonts.googleapis.com/css2?family=Poppins:wght@300;400;500;600;700;800&family=Roboto+Condensed:wght@700&display=swap" rel="stylesheet">
<style>
  :root{
    --navy:#0c2a5b;
    --navy-deep:#0a2550;
    --red:#e8392f;
    --paper:#f1f2f4;
    --ink:#0c2a5b;
    --muted:#5a6070;
    --line:#cfd3da;
  }
  *{box-sizing:border-box;margin:0;padding:0}
  html,body{width:972px;height:1200px;overflow:hidden}
  body{font-family:"Poppins",sans-serif;color:var(--ink);background:var(--paper)}
  .flyer{position:relative;width:972px;height:1200px;overflow:hidden;background:var(--paper)}
  .abs{position:absolute}

  .brand{left:47px;top:52px;display:flex;align-items:center;gap:14px}
  .brand-mark{width:44px;height:44px;background:var(--red)}
  .brand-name{font-size:36px;font-weight:800;color:var(--navy);line-height:1;letter-spacing:-.5px}
  .brand-tag{left:106px;top:94px;font-size:11px;font-weight:600;color:var(--navy)}

  .headline{left:47px;top:158px;font-size:47px;line-height:51px;color:var(--navy);text-transform:uppercase}
  .headline .light{font-weight:300}
  .headline .bold{font-weight:800}

  .intro{left:47px;top:380px;width:320px;font-size:17px;line-height:23px;font-weight:400;color:#1e2233}
  .intro strong{color:var(--red);font-weight:600}

  .hero-shot{left:405px;top:262px;width:530px;height:340px;border-radius:6px;
    background:linear-gradient(135deg,#e9ebef 0%,#d6dae1 45%,#bfc6d2 100%)}

  .price-badge{left:767px;top:526px;width:140px;height:140px;border-radius:50%;background:#fff;
    box-shadow:0 6px 12px rgba(0,0,0,.25);display:flex;align-items:center;justify-content:center}
  .price-inner{width:124px;height:124px;border-radius:50%;background:var(--red);color:#fff;text-align:center;
    display:flex;flex-direction:column;justify-content:center}
  .price-inner .amt{font-family:"Roboto Condensed",sans-serif;font-weight:700;font-size:32px;line-height:1}
  .price-inner .lbl{font-size:13px;line-height:14px;margin-top:6px;font-weight:400}

  .section-tab{left:45px;top:572px;width:222px;height:44px;background:var(--navy);color:#fff;
    font-size:23px;font-weight:600;padding:6px 0 0 13px;clip-path:polygon(0 0,88% 0,100% 100%,0 100%)}
  .section-rule{left:45px;top:614px;width:412px;height:2px;background:linear-gradient(90deg,var(--navy),rgba(12,42,91,0))}

  .product{display:flex;align-items:center;gap:14px;font-size:17px;line-height:20px;font-weight:400;color:var(--navy)}
  .product svg{flex:none}

  .feature{text-align:center;font-size:11px;font-weight:400;color:var(--navy)}
  .feature .ph{width:100%;height:72px;border-radius:4px;margin-bottom:10px;background:linear-gradient(160deg,#dfe3ea,#b9c1ce)}
  .vsep{width:1px;background:var(--line)}

  .plan-box{left:583px;top:716px;width:251px;height:283px;border:2px solid var(--red);border-top:none;border-radius:0 0 16px 16px}
  .plan-box-top{left:775px;top:716px;width:59px;height:16px;border-top:2px solid var(--red);border-right:2px solid var(--red);border-radius:0 14px 0 0}
  .plan-tab{left:570px;top:699px;width:253px;height:44px;background:var(--red);color:#fff;font-size:19px;font-weight:500;
    padding:8px 0 0 12px;border-radius:0 22px 22px 0}
  .plan-list{left:570px;top:772px;width:270px;list-style:none}
  .plan-list li{display:flex;gap:12px;font-size:20px;line-height:24px;color:var(--navy);margin-bottom:12px}
  .plan-list .num{flex:none;width:24px;height:24px;border-radius:50%;background:var(--red);color:#fff;font-size:15px;
    font-weight:700;display:flex;align-items:center;justify-content:center;margin-top:2px}

  .cta{left:593px;top:1030px;width:302px;text-align:center}
  .cta-top{display:flex;align-items:center;gap:8px;color:var(--red);font-size:17px;font-weight:600}
  .cta-top::before,.cta-top::after{content:"";flex:1;height:1px;background:var(--red)}
  .cta-main{background:var(--navy);color:#fff;font-size:17px;font-weight:600;padding:2px 0;margin-top:-2px}
  .cta-note{font-size:11.5px;color:var(--muted);margin-top:6px;font-weight:300}

  .footer-band{left:0;top:1146px;width:972px;height:54px;background:var(--navy)}
  .footer-call{left:0;top:1116px;width:420px;height:84px;background:var(--red);color:#fff;padding:8px 0 0 37px;
    clip-path:polygon(0 0,80% 0,100% 100%,0 100%);border-radius:0 0 0 0}
  .footer-call .small{font-size:17px;font-weight:400;line-height:20px}
  .footer-call .phone{display:flex;align-items:center;gap:8px;font-size:28px;font-weight:700;line-height:36px}
  .contact{top:1163px;display:flex;align-items:center;gap:7px;color:#fff;font-size:16px;font-weight:400}
  .contact b{font-weight:700}
  .dot{width:13px;height:13px;border-radius:50%;background:var(--red)}
</style>
</head>
<body>
<main class="flyer">

  <!-- right navy panel with red edge -->
  <svg class="abs" style="left:0;top:0" width="972" height="1200" aria-hidden="true">
    <polygon points="700,0 972,0 972,660 764,520 606,278" fill="var(--red)"/>
    <polygon points="712,0 972,0 972,646 770,512 618,276" fill="var(--navy)"/>
  </svg>

  <div class="abs brand">
    <span class="brand-mark"></span>
    <span class="brand-name">THE WATCHPOST DEPOT</span>
  </div>

  <h1 class="abs headline">
    <span class="light">Makes your</span><br>
    <span class="bold">Security simple</span><br>
    <span class="bold">for years</span><br>
    <span class="light">to come.</span>
  </h1>

  <p class="abs intro">With over <strong>20 years experience</strong> and an ever growing list of clients, The Watchpost Depot is the right integrator for your next security project</p>

  <div class="abs hero-shot" role="img" aria-label="Product photo: office door, bullet camera, dome camera and a monitor showing surveillance software"></div>

  <div class="abs price-badge">
    <div class="price-inner">
      <span class="amt">$299/yr</span>
      <span class="lbl">Annual<br>Service Plan</span>
    </div>
  </div>

  <h2 class="abs section-tab">Our Products</h2>
  <div class="abs section-rule"></div>

  <div class="abs product" style="left:40px;top:650px">
    <svg width="56" height="56" viewBox="0 0 56 56"><circle cx="28" cy="28" r="26" fill="none" stroke="var(--red)" stroke-width="2"/><rect x="15" y="23" width="22" height="11" rx="2" fill="var(--red)" transform="rotate(-18 26 28)"/><rect x="36" y="26" width="6" height="6" fill="var(--red)"/></svg>
    <span>Security Camera<br>System</span>
  </div>
  <div class="abs product" style="left:294px;top:646px">
    <svg width="56" height="56" viewBox="0 0 56 56"><circle cx="28" cy="28" r="26" fill="none" stroke="var(--red)" stroke-width="2"/><rect x="18" y="15" width="20" height="26" rx="3" fill="none" stroke="var(--red)" stroke-width="2.5"/><rect x="22" y="19" width="12" height="5" fill="var(--red)"/><g fill="var(--red)"><rect x="22" y="27" width="3" height="3"/><rect x="27" y="27" width="3" height="3"/><rect x="32" y="27" width="3" height="3"/><rect x="22" y="32" width="3" height="3"/><rect x="27" y="32" width="3" height="3"/><rect x="32" y="32" width="3" height="3"/></g></svg>
    <span>Intrusion<br>Alarm</span>
  </div>
  <div class="abs product" style="left:40px;top:730px">
    <svg width="56" height="56" viewBox="0 0 56 56"><circle cx="28" cy="28" r="26" fill="none" stroke="var(--red)" stroke-width="2"/><line x1="10" y1="10" x2="46" y2="46" stroke="var(--red)" stroke-width="2"/><circle cx="34" cy="22" r="6" fill="var(--red)"/><line x1="30" y1="26" x2="16" y2="40" stroke="var(--red)" stroke-width="4"/></svg>
    <span>Access Control<br>&amp; Intercom</span>
  </div>
  <div class="abs product" style="left:294px;top:730px">
    <svg width="56" height="56" viewBox="0 0 56 56"><circle cx="28" cy="28" r="26" fill="none" stroke="var(--red)" stroke-width="2"/><rect x="14" y="22" width="28" height="18" fill="none" stroke="var(--red)" stroke-width="2.5"/><line x1="21" y1="22" x2="21" y2="40" stroke="var(--red)" stroke-width="2"/><line x1="28" y1="22" x2="28" y2="40" stroke="var(--red)" stroke-width="2"/><line x1="35" y1="22" x2="35" y2="40" stroke="var(--red)" stroke-width="2"/><line x1="14" y1="31" x2="42" y2="31" stroke="var(--red)" stroke-width="2"/><path d="M34 12l7 3v5c0 4-3 6-7 8-4-2-7-4-7-8v-5z" fill="var(--red)"/></svg>
    <span>Perimeter<br>Security</span>
  </div>

  <div class="abs feature" style="left:30px;top:838px;width:120px"><div class="ph" role="img" aria-label="Monitor showing video management software"></div>Easy to use Software</div>
  <div class="abs vsep" style="left:164px;top:838px;height:104px"></div>
  <div class="abs feature" style="left:180px;top:838px;width:120px"><div class="ph" role="img" aria-label="Multi-sensor dome camera"></div>High Definition</div>
  <div class="abs vsep" style="left:326px;top:838px;height:104px"></div>
  <div class="abs feature" style="left:346px;top:838px;width:130px"><div class="ph" role="img" aria-label="Laptop, tablet and phone showing remote camera views"></div>Remote Access</div>

  <div class="abs feature" style="left:30px;top:960px;width:120px"><div class="ph" role="img" aria-label="Technician holding a hard hat"></div>Experience</div>
  <div class="abs vsep" style="left:164px;top:960px;height:104px"></div>
  <div class="abs feature" style="left:180px;top:960px;width:120px"><div class="ph" role="img" aria-label="Keypad reader, phone and access cards"></div>Access Control</div>
  <div class="abs vsep" style="left:326px;top:960px;height:104px"></div>
  <div class="abs feature" style="left:346px;top:960px;width:130px"><div class="ph" role="img" aria-label="Alarm keypad panel"></div>Intrusion Alarm</div>

  <div class="abs vsep" style="left:533px;top:640px;height:460px"></div>

  <div class="abs plan-box"></div>
  <div class="abs plan-box-top"></div>
  <h3 class="abs plan-tab">Service plan includes</h3>
  <ol class="abs plan-list">
    <li><span class="num">1</span><span>Discounted service rate of $118/hr</span></li>
    <li><span class="num">2</span><span>Free remote support ($85/hr without a plan)</span></li>
    <li><span class="num">3</span><span>Free remote training</span></li>
    <li><span class="num">4</span><span>Priority support</span></li>
  </ol>

  <div class="abs cta">
    <div class="cta-top">SIGN UP FOR OUR</div>
    <div class="cta-main">ANNUAL SERVICE PLAN</div>
    <div class="cta-note">The plan will automatically renew every year</div>
  </div>

  <div class="abs footer-band"></div>
  <div class="abs footer-call">
    <div class="small">For Free Quote CALL</div>
    <div class="phone">
      <svg width="22" height="22" viewBox="0 0 24 24"><path d="M6.6 10.8c1.4 2.8 3.8 5.1 6.6 6.6l2.2-2.2c.3-.3.7-.4 1-.2 1.1.4 2.3.6 3.6.6.6 0 1 .4 1 1V20c0 .6-.4 1-1 1C10.6 21 3 13.4 3 4c0-.6.4-1 1-1h3.5c.6 0 1 .4 1 1 0 1.3.2 2.5.6 3.6.1.3 0 .7-.2 1z" fill="#fff"/></svg>
      1-877-555-0142
    </div>
  </div>
  <div class="abs contact" style="left:453px"><span class="dot"></span>www.<b>kelvamart</b>.com</div>
  <div class="abs contact" style="left:665px"><span class="dot"></span>sales@kelvamart.com</div>

</main>
</body>
</html>
```